Flyer Rework for Accountants and Lawyers

Information flyer for accountants and lawyers. Text and flowchart provided. Just need to make it look presentable for print and email. Needs to add logo (AI file provided) and provide graphics. No more than two pages. Our corporate visual identify guidelines are attached (MUST Use). Completed on both AI file and PPTX file.
Target Market(s)
Accountants, Company Directors and Lawyers
Industry/Entity Type
Finance And Accounting
Requirements
Must have
- Our corporate visual identify guidelines are attached (MUST Use)

```html
<!DOCTYPE html>
<html lang="en">
<head>
<meta charset="utf-8">
<title>Fernbrook Advisory – Director Penalty Notices</title>
<link href="https://fonts.googleapis.com/css2?family=Montserrat:wght@400;500;600&family=Arimo:wght@400;700&display=swap" rel="stylesheet">
<style>
  :root{
    --green:#6cbd45;
    --grey:#6d6e71;
    --grey-dark:#58595b;
    --bg:#a7a9ac;
    --row:#f1f1f2;
    --text:#414042;
    --white:#ffffff;
  }
  *{margin:0;padding:0;box-sizing:border-box}
  html,body{width:789px;height:1200px;overflow:hidden}
  body{background:var(--bg);font-family:"Arimo",Arial,sans-serif;color:var(--text);position:relative}
  .page{position:absolute;left:48px;width:688px;height:535px;background:var(--white);overflow:hidden;box-shadow:3px 4px 8px rgba(0,0,0,.35)}
  .page--one{top:48px}
  .page--two{top:614px}
  .abs{position:absolute}
  .art{position:absolute;left:0;top:0}

  /* page one */
  .brand{left:42px;top:42px;display:flex;align-items:center;gap:10px}
  .brand__mark{width:58px;height:58px;border-radius:50%;background:var(--green)}
  .brand__name{font-family:"Montserrat",sans-serif;font-weight:500;font-size:19px;color:var(--green);letter-spacing:.2px;line-height:1}
  .brand__tag{font-family:"Montserrat",sans-serif;font-size:9.5px;color:var(--grey);margin-top:4px;margin-left:13px}
  .headline{left:46px;top:121px;font-family:"Montserrat",sans-serif;font-weight:500;font-size:15.5px;color:var(--green);letter-spacing:.2px}
  .intro{left:46px;top:148px;width:300px;font-size:7.2px;line-height:10px}
  .subhead{left:46px;top:188px;font-size:8.5px;font-weight:700;color:var(--green)}
  .intro--dpn{top:199px;width:318px}
  .band-grey{left:0;top:249px;width:688px;height:31px;background:var(--grey)}
  .band-grey p{position:absolute;left:51px;top:6px;color:var(--white);font-size:7.4px;line-height:10px}
  .band-green{left:0;top:472px;width:688px;height:63px;background:var(--green)}
  .contact{left:0;top:504px;width:688px;text-align:center;color:var(--white);font-weight:700;font-size:8.6px}

  .facts{position:absolute;left:51px;top:294px;width:598px;border-collapse:collapse;font-size:7px;line-height:10px;table-layout:fixed}
  .facts th{background:var(--green);color:var(--white);font-weight:700;height:17px;font-size:7px;border-right:2px solid var(--white)}
  .facts th:last-child{border-right:none}
  .facts td{vertical-align:top;padding:4px 5px}
  .facts td:first-child{padding-left:20px;padding-right:2px}
  .facts tbody tr:nth-child(odd) td{background:var(--row)}
  .facts tbody tr:nth-child(even) td{background:var(--white)}
  .facts .n{display:inline-block;width:14px}
  .facts ul{list-style:none;margin-top:1px}
  .facts li{padding-left:30px;position:relative;line-height:9.5px}
  .facts li::before{content:"";position:absolute;left:18px;top:3px;width:4px;height:4px;background:var(--green)}

  /* page two */
  .tips-bg{left:0;top:0;width:688px;height:187px;background:var(--grey)}
  .tips-title{left:261px;top:26px;color:var(--white);font-size:10.5px;font-weight:700}
  .tip{position:absolute;left:272px;display:flex;gap:10px;color:var(--white);font-size:7.2px;line-height:10px;width:388px}
  .tip svg{flex:0 0 22px}
  .tip b{font-weight:700}
  .summary{left:194px;top:206px;font-family:"Montserrat",sans-serif;font-weight:500;font-size:16px;color:var(--green);letter-spacing:.3px}
  .box{position:absolute;border:1.3px solid var(--green);border-radius:9px;display:flex;align-items:center;justify-content:center;text-align:center;font-size:7.6px;line-height:10px;font-weight:700;color:var(--grey);padding:6px 14px}
  .box--list{display:block;text-align:left;padding:7px 10px}
  .box ol{margin-left:26px;margin-top:1px}
  .flow-label{position:absolute;font-size:7.5px;font-weight:700;color:var(--grey)}
  .band-help{left:0;top:450px;width:688px;height:85px;background:var(--green);color:var(--white)}
  .band-help h2{position:absolute;left:38px;top:20px;font-size:9.5px;font-weight:700}
  .band-help p{position:absolute;left:38px;top:43px;width:610px;font-size:7px;line-height:10px}
</style>
</head>
<body>

<section class="page page--one">
  <svg class="art" width="688" height="535" viewBox="0 0 688 535">
    <defs>
      <clipPath id="photo-one"><circle cx="538" cy="126" r="140"/></clipPath>
      <linearGradient id="tone-one" x1="0" y1="0" x2="1" y2="1">
        <stop offset="0" stop-color="#d9cbb8"/><stop offset=".55" stop-color="#eeeae6"/><stop offset="1" stop-color="#c9ccd2"/>
      </linearGradient>
    </defs>
    <rect x="390" y="-20" width="300" height="300" fill="url(#tone-one)" clip-path="url(#photo-one)" role="img" aria-label="Photo: hands pointing at a printed document with a pen"/>
    <path d="M 424 214 A 146 146 0 0 0 672 188" fill="none" stroke="var(--green)" stroke-width="12"/>
    <path d="M 402 120 A 146 146 0 0 0 424 214" fill="none" stroke="var(--green)" stroke-width="12"/>
    <path d="M 412 52 A 146 146 0 0 1 672 60" fill="none" stroke="var(--grey)" stroke-width="12"/>
    <rect x="387" y="69" width="150" height="24" fill="var(--grey)"/>
    <rect x="574" y="128" width="114" height="25" fill="var(--green)"/>
  </svg>

  <div class="abs brand">
    <span class="brand__mark"></span>
    <div>
      <div class="brand__name">FERNBROOK ADVISORY</div>
      <div class="brand__tag">Restructuring &amp; Solvency Accountants</div>
    </div>
  </div>

  <h1 class="abs headline">INDEPENDENT. CONCISE. EFFICIENT.</h1>
  <p class="abs intro">Company directors and their advisors need to be aware that non-lodgement of Business Activities Statements (“BAS”) and Superannuation Guarantee Charge (“SCG”) Statements with the ATO may be personally liability for these debts.</p>
  <h2 class="abs subhead">Director Penalty Notices (“DPN”)</h2>
  <p class="abs intro intro--dpn">The ATO uses DPNs and Garnishee Notices to recovery tax debts and to impose positive obligations on Directors to deal with outstanding PAYG Withholding and the Superannuation Guarantee Charge debts (“Tax Debts”).</p>

  <div class="abs band-grey"><p>The DPN regime makes directors of companies who fail to pay Tax Debts personally liable.<br>The key facts of DPN regime are outlined below:</p></div>
  <div class="abs band-green"></div>

  <table class="facts">
    <colgroup><col style="width:132px"><col></colgroup>
    <thead><tr><th>Facts</th><th>Key facts of a Directors Penalty Notice</th></tr></thead>
    <tbody>
      <tr style="height:29px"><td><span class="n">1.</span>Director personal<br><span class="n"></span>liabilities</td><td>Directors become personally liable for Tax Debts 21 days are the DPN Notice is issued</td></tr>
      <tr style="height:42px"><td><span class="n">2.</span>Automatic liability for<br><span class="n"></span>unreported and unpaid<br><span class="n"></span>Tax Debts</td><td>Where a company’s Tax Debts were both unreported and unpaid 3 months after the due date, the directors are automatically personally liable for the Tax Debts.</td></tr>
      <tr style="height:61px"><td><span class="n">3.</span>Avoiding personal<br><span class="n"></span>liability for directors<br><span class="n"></span>once they receive a<br><span class="n"></span>DPN</td><td>Within 21 days of issuing the DPN (which may be received a week or more after issue), a director can avoid personal liability by either:
        <ul><li>Paying the Tax Debt</li><li>Appointing an Administrator to the company</li><li>Appointing a Liquidator to the company.</li></ul></td></tr>
      <tr style="height:17px"><td><span class="n">4.</span>Effect on new directors</td><td>New directors are liable if outstanding Tax Debts are unpaid 30 days after their appointment as director</td></tr>
      <tr style="height:29px"><td><span class="n">5.</span>Time frames</td><td>ATO can only enforce a DPN after 21 days of giving notice to the director and notice can be given to the company tax agent</td></tr>
    </tbody>
  </table>

  <p class="abs contact">Call (02) 5550 1234 &nbsp;|&nbsp; email info@fernbrookadvisory.com.au | fernbrookadvisory.com.au.</p>
</section>

<section class="page page--two">
  <div class="abs tips-bg"></div>
  <svg class="art" width="688" height="535" viewBox="0 0 688 535">
    <defs>
      <clipPath id="photo-two"><circle cx="108" cy="92" r="138"/></clipPath>
      <linearGradient id="tone-two" x1="0" y1="0" x2="1" y2="1">
        <stop offset="0" stop-color="#b9bcc0"/><stop offset=".5" stop-color="#ecedee"/><stop offset="1" stop-color="#d8d2c8"/>
      </linearGradient>
    </defs>
    <rect x="-40" y="-50" width="300" height="290" fill="url(#tone-two)" clip-path="url(#photo-two)" role="img" aria-label="Photo: business meeting around a table with charts and papers"/>
    <path d="M 0 196 A 150 150 0 0 0 165 231" fill="none" stroke="var(--green)" stroke-width="12"/>
    <path d="M 165 231 A 150 150 0 0 0 226 0" fill="none" stroke="var(--white)" stroke-width="12"/>
    <rect x="86" y="96" width="130" height="23" fill="var(--green)"/>
  </svg>

  <h2 class="abs tips-title">Tips for directors to limit or avoid personal liability:</h2>
  <div class="tip" style="top:52px">
    <svg width="22" height="22" viewBox="0 0 22 22" fill="none" stroke="#fff" stroke-width="1.2"><rect x="2" y="4" width="18" height="16"/><line x1="2" y1="8" x2="20" y2="8"/><line x1="6" y1="2" x2="6" y2="6"/><line x1="16" y1="2" x2="16" y2="6"/><path d="M5 11h3M10 11h3M15 11h2M5 14h3M10 14h3M15 14h2M5 17h3M10 17h3"/></svg>
    <p><b>Always lodge BAS and SGC Statements within 3 months of the due date,</b> even if the liability cannot be paid!</p>
  </div>
  <div class="tip" style="top:83px">
    <svg width="22" height="22" viewBox="0 0 22 22"><circle cx="13" cy="6" r="5" fill="#fff"/><text x="13" y="9" font-size="7" text-anchor="middle" fill="#6d6e71" font-family="Arimo">$</text><path d="M1 16c3-3 6-3 9-1h5c1 0 1 2 0 2h-5M1 20c3-1 8 1 12 0l7-4" fill="none" stroke="#fff" stroke-width="1.3"/></svg>
    <p><b>Act immediately upon receipt of a DPN and consider a payment arrangement with the ATO.</b> This should be considered with care as payments made can be considered as preference payments to the ATO, if a liquidator is appointed. The ATO can make the directors personally liable for the ATO preference claim</p>
  </div>
  <div class="tip" style="top:134px">
    <svg width="22" height="22" viewBox="0 0 22 22" fill="none" stroke="#fff" stroke-width="1.2"><path d="M11 4a5 5 0 0 0-3 9v3h6v-3a5 5 0 0 0-3-9z" fill="#fff"/><line x1="9" y1="18" x2="13" y2="18"/><path d="M11 0v2M3 7h2M17 7h2M5 2l1.5 1.5M17 2l-1.5 1.5"/></svg>
    <p><b>Seek professional advice from an insolvency practitioner about the options available and possibly save the company through a financial restructure.</b></p>
  </div>

  <h2 class="abs summary">SUMMARY OF THE DPN</h2>

  <svg class="art" width="688" height="535" viewBox="0 0 688 535" fill="none" stroke="#6d6e71" stroke-width="1">
    <path d="M153 318h26M176 315l3 3-3 3"/>
    <path d="M288 298h26M311 295l3 3-3 3"/>
    <path d="M288 347h26M311 344l3 3-3 3"/>
    <path d="M448 287h26M471 284l3 3-3 3"/>
    <path d="M598 327v11M595 335l3 3 3-3"/>
    <path d="M536 321v42h-88M451 360l-3 3 3 3"/>
  </svg>

  <div class="box" style="left:48px;top:269px;width:95px;height:95px">Issued Director’s Penalty Notice By ATO</div>
  <div class="box" style="left:183px;top:269px;width:95px;height:95px;padding:6px 8px">Business Activity Statement and Superannuation Guarantee Charge lodged within 3 months from due date</div>
  <div class="box" style="left:324px;top:246px;width:119px;height:79px">Director not personally liable yet.<br>(Have options)<br>[RIGHTS PRESERVED]</div>
  <div class="box box--list" style="left:480px;top:243px;width:168px;height:78px">If Directors act within 21 days and:
    <ol><li>Wind up Company voluntarily; or</li><li>Appoint Voluntary Administrator; or</li><li>Pay debt in full</li></ol></div>
  <div class="box" style="left:324px;top:338px;width:119px;height:78px;padding:6px 30px">Director Automatically personally liable</div>
  <div class="box" style="left:528px;top:346px;width:120px;height:78px">Director not personally liable but the company is still insolvent.</div>
  <span class="flow-label" style="left:295px;top:283px">No</span>
  <span class="flow-label" style="left:293px;top:333px">Yes</span>
  <span class="flow-label" style="left:576px;top:327px">Yes</span>
  <span class="flow-label" style="left:509px;top:351px">No</span>

  <div class="abs band-help">
    <h2>How Fernbrook Advisory can help?</h2>
    <p>Fernbrook Advisory is a firm that specialises in insolvency and restructuring, we are here to assist your clients who experiencing financial difficulties with straight forward solutions in simple to understand terms. The initial consultation is free, strictly confidential and without obligation. Please call (02) 5550 1234 to speak to one of our solvency specialist or email info@fernbrookadvisory.com.au.</p>
  </div>
</section>

</body>
</html>
```